Classy, Elegant, Simple Business Card Design

Looking to have a classy, simple, and elegant design. Want a top notch designed business card. I really like the look of the new brivo credit card. I also like the design I attached. I am trying to reach 21-29 year old females for booking us for there wedding or event. We offer Disc Jockey Service, Photo Booth Rentals, and Uplighting .

Target Market(s)

21-28 year old females

Contact Information for Business Card

Has to have logo, website, email, and phone number

Font styles to use
Other font styles liked:
• open to font choice, modern, clean
Designer to choose
33a6d7
0791cd
0555a3
ffffff

Requirements
Must have
• Has to have logo, website, email, and phone number
Nice to have
• I really like the design of the new brivo credit card. I also included my logo and some designs I like
Should not have
• clutter or too much info

```html
<!DOCTYPE html>
<html lang="en">
<head>
<meta charset="UTF-8">
<title>Tidelight — Business Card</title>
<link rel="stylesheet" href="https://fonts.googleapis.com/css2?family=Roboto:wght@400;700&display=swap">
<style>
  :root {
    --backdrop: #c6d4d4;
    --card: #ffffff;
    --card-shade: #eef0f2;
    --brand-blue: #0791cd;
    --band-blue: #1a8ad4;
    --deep-blue: #0555a3;
    --ink: #4a4d52;
  }
  * { margin: 0; padding: 0; box-sizing: border-box; }
  html, body {
    width: 1200px;
    height: 800px;
    overflow: hidden;
    background: var(--backdrop);
    font-family: "Roboto", Arial, sans-serif;
  }
  .stage {
    width: 1200px;
    height: 800px;
    display: flex;
    align-items: center;
    justify-content: center;
  }
  .business-card {
    position: relative;
    width: 700px;
    height: 400px;
    background: var(--card);
    overflow: hidden;
    box-shadow: 0 18px 40px rgba(60, 80, 80, 0.18);
  }
  .wave-backdrop {
    position: absolute;
    inset: 0 0 14px 0;
    background: linear-gradient(120deg, var(--card) 0%, var(--card) 35%, var(--card-shade) 100%);
  }
  .brand {
    position: absolute;
    top: 52px;
    left: 56px;
    display: flex;
    align-items: center;
    gap: 12px;
  }
  .brand-dot {
    width: 34px;
    height: 34px;
    border-radius: 50%;
    background: var(--brand-blue);
  }
  .brand-text { display: flex; flex-direction: column; }
  .brand-name {
    font-weight: 700;
    font-size: 22px;
    letter-spacing: 1px;
    color: var(--deep-blue);
    text-transform: uppercase;
  }
  .brand-tagline {
    font-weight: 700;
    font-size: 9px;
    letter-spacing: 3px;
    color: var(--deep-blue);
    text-transform: uppercase;
    margin-top: 2px;
  }
  .contact-list {
    position: absolute;
    left: 56px;
    bottom: 70px;
    list-style: none;
  }
  .contact-item {
    display: flex;
    align-items: center;
    gap: 14px;
    font-size: 21px;
    color: var(--ink);
    line-height: 1;
    margin-top: 9px;
  }
  .contact-icon {
    width: 20px;
    height: 20px;
    border-radius: 50%;
    background: var(--band-blue);
    display: flex;
    align-items: center;
    justify-content: center;
    flex-shrink: 0;
  }
  .contact-icon svg { width: 12px; height: 12px; }
  .accent-band {
    position: absolute;
    left: 0;
    right: 0;
    bottom: 0;
    height: 14px;
    background: var(--band-blue);
  }
</style>
</head>
<body>
<main class="stage">
  <section class="business-card">
    <div class="wave-backdrop" role="img" aria-label="Soft white and pale grey flowing wave pattern across the card"></div>

    <div class="brand">
      <span class="brand-dot"></span>
      <div class="brand-text">
        <span class="brand-name">Tidelight</span>
        <span class="brand-tagline">Event Services</span>
      </div>
    </div>

    <ul class="contact-list">
      <li class="contact-item">
        <span class="contact-icon">
          <svg viewBox="0 0 12 12"><rect x="3.5" y="1" width="5" height="10" rx="1" fill="none" stroke="#fff" stroke-width="1.2"/></svg>
        </span>
        202-555-0148
      </li>
      <li class="contact-item">
        <span class="contact-icon">
          <svg viewBox="0 0 12 12"><rect x="1.5" y="3" width="9" height="6.5" fill="none" stroke="#fff" stroke-width="1.2"/><path d="M1.5 3 L6 7 L10.5 3" fill="none" stroke="#fff" stroke-width="1.2"/></svg>
        </span>
        hello@tidelightevents.com
      </li>
      <li class="contact-item">
        <span class="contact-icon">
          <svg viewBox="0 0 12 12"><circle cx="6" cy="6" r="4.5" fill="none" stroke="#fff" stroke-width="1.1"/><ellipse cx="6" cy="6" rx="2" ry="4.5" fill="none" stroke="#fff" stroke-width="1"/><path d="M1.5 6 H10.5" stroke="#fff" stroke-width="1"/></svg>
        </span>
        www.tidelightevents.com
      </li>
    </ul>

    <div class="accent-band"></div>
  </section>
</main>
</body>
</html>
```